Need Professional, Modern, Clean Newsletter Templates for High End Real Estate Agents in Orange Coun

I need a newsletter for realtors who specialize in high-end home sales for Orange County, California. Please see the attached draft of the newsletter we have in mind. Please note the logo at the top and the beach imagery and please use these and complementary fonts, colors and themes when creating your design. These particular realtors focus on very high-end clients with a specialization on ocean front properties. I WANT YOU TO PLEASE USE THE HEADER FROM MY ATTACHMENT IN YOUR NEWSLETTER. THIS NEWSLETTER IS INTENDED TO BE SENT OUT VIA EMAIL ONLY, NOT PRINT.

The idea behind the newsletter is that it will cover four broad categories. We will have a content creator who will pull content each week, however we need a nice looking template that can support their content. These are the four categories :

1) Market Data - this will pull graphs and information that the realtors receive, directly from the MLS (home listing site). Most of this will be in graph or table form, so we need a nice way to support that.

2.) Featured Listings - this will show the featured homes they have for sale at any given time. This section of the template should have a place to put pictures of the home with supporting text.

3.) News you can use - links to videos and articles relevant to the real estate industry and in the area.

4.) Upcoming OC Events - list of upcoming events in the area.
Updates

I feel like I need to post this update in case there was some confusion in my contest brief.

I DO NOT want a new logo or header design. What I am looking for is a newsletter to support the header and logo I already have, and for a nice template which includes each of the four sections I described in my brief. I would like you to think about each of the four sections and design them accordingly. There needs to be a good section for graphs (market data), for videos, for featured listings (pictures of homes with supporting descriptive text) and upcoming events (maybe supported by a calendar and text sections to describe the event, etc.)

This newsletter will be sent out as email only. Your entries should be made as .pdf or as a word document. Thanks.

Target Market(s)

High end real estate buyers and sellers, with a focus on ocean front property.

Industry/Entity Type

Real Estate

Colors
33a6d7
00a990
86cae6

Requirements
Must have
• You MUST include the header photo from the .png attachment I included. "Varnell at the Shore - Sell with the Best."

```html
<!DOCTYPE html>
<html lang="en">
<head>
<meta charset="utf-8">
<title>Varnell at the Shore - Sell with the Best.</title>
<link rel="stylesheet" href="https://fonts.googleapis.com/css2?family=Montserrat:wght@500;600&family=Open+Sans:wght@400;600;700&family=Arimo:wght@400;700&display=swap">
<style>
  :root {
    --page-bg: #efefef;
    --sheet-bg: #ffffff;
    --teal: #1aa3c0;
    --teal-dark: #1d6f80;
    --text-gray: #6f6f6f;
    --text-dark: #111111;
    --muted: #b5b5b5;
    --rule: #e4e4e4;
    --table-head: #dcdcdc;
    --footer-bg: #545359;
    --footer-text: #ffffff;
    --footer-muted: #b9b8bd;
    --icon-bg: #dddddd;
    --icon-ink: #555555;
  }
  * { box-sizing: border-box; margin: 0; padding: 0; }
  html, body { width: 1200px; height: 2546px; overflow: hidden; background: var(--page-bg); }
  body { font-family: "Arimo", Arial, sans-serif; position: relative; }

  .sheet { position: absolute; left: 239px; top: 0; width: 720px; height: 2546px; background: var(--sheet-bg); }
  .abs { position: absolute; }

  .header-photo {
    left: 0; top: 0; width: 720px; height: 263px;
    background: linear-gradient(180deg, #6fa6d2 0%, #3bb3c6 45%, #8fd3dc 72%, #ffffff 100%);
  }
  .brand-name {
    left: 53px; top: 88px; font-family: "Open Sans", Arial, sans-serif; font-weight: 400;
    font-size: 30px; color: #ffffff; letter-spacing: 0.5px;
  }
  .tagline {
    left: 405px; top: 114px; font-family: "Open Sans", Arial, sans-serif; font-weight: 400;
    font-size: 19px; color: #ffffff; letter-spacing: 0.3px;
  }

  .section-title {
    font-family: "Montserrat", Arial, sans-serif; font-weight: 600; font-size: 27px;
    color: var(--teal); letter-spacing: 0.3px; line-height: 1;
  }
  .body-text { font-size: 15.6px; line-height: 24.2px; color: var(--text-gray); }
  .rule { left: 38px; width: 645px; height: 2px; background: var(--rule); }

  .agent-photo { left: 525px; top: 306px; width: 153px; height: 197px; background: linear-gradient(160deg, #3a2a22, #5b4536 55%, #2d211b); }
  .agent-name { left: 525px; width: 153px; top: 514px; text-align: center; font-weight: 700; font-size: 15px; color: var(--muted); }
  .agent-email { left: 525px; width: 153px; top: 540px; text-align: center; font-size: 12.5px; color: var(--muted); text-decoration: underline; }

  .snapshot-title { left: 0; width: 720px; top: 792px; text-align: center; font-weight: 700; font-size: 21px; color: var(--text-dark); }
  .market-table { left: 33px; top: 826px; width: 658px; border-collapse: collapse; font-size: 15.5px; color: var(--text-dark); }
  .market-table th { background: var(--table-head); color: var(--teal-dark); font-weight: 700; height: 24px; }
  .market-table td { height: 24px; text-align: center; }
  .market-table .label { text-align: right; padding-right: 12px; width: 188px; }
  .market-table .trend-row td { height: 44px; vertical-align: bottom; }
  .trend { display: inline-block; text-align: center; }
  .trend svg { display: block; margin: 0 auto 2px; }
  .trend a { color: var(--teal-dark); font-size: 15.5px; text-decoration: underline; }

  .listing-photo { left: 39px; width: 263px; height: 197px; background: linear-gradient(180deg, #3c7ad8 0%, #8fb3dc 40%, #b9a98a 65%, #6e6a58 100%); }
  .listing-title { left: 318px; font-weight: 700; font-size: 15.5px; color: var(--text-dark); }
  .listing-text { left: 318px; width: 355px; }
  .read-more { font-weight: 700; font-size: 13.5px; color: var(--text-gray); text-decoration: underline; letter-spacing: 0.3px; }

  .news-title { left: 41px; font-weight: 700; font-size: 15.5px; color: var(--text-dark); }
  .news-text { left: 41px; width: 620px; }

  .event { display: flex; gap: 14px; width: 310px; }
  .event-date {
    flex: none; width: 56px; height: 56px; background: var(--teal); color: #fff; text-align: center;
    font-weight: 700; font-size: 12px; line-height: 1; padding-top: 9px;
  }
  .event-date b { display: block; font-size: 22px; margin-top: 3px; }
  .event-title { font-weight: 700; font-size: 15.5px; color: var(--text-dark); margin-top: 4px; }
  .event-text { font-size: 14.5px; line-height: 22px; color: var(--text-gray); margin-top: 4px; }

  .connect-title { left: 38px; top: 2240px; font-family: "Open Sans", Arial, sans-serif; font-weight: 700; font-size: 21px; color: #3d3d3d; }
  .social-list { left: 270px; top: 2231px; display: flex; gap: 12px; }
  .social-dot { width: 41px; height: 41px; border-radius: 50%; background: var(--icon-bg); display: flex; align-items: center; justify-content: center; }
  .social-dot svg { width: 20px; height: 20px; fill: none; stroke: var(--icon-ink); stroke-width: 2; stroke-linecap: round; stroke-linejoin: round; }

  .footer { left: 0; top: 2300px; width: 720px; height: 246px; background: var(--footer-bg); }
  .footer-text { left: 38px; top: 44px; width: 620px; font-size: 15.5px; line-height: 24.5px; color: var(--footer-text); }
  .footer-rule { left: 38px; top: 174px; width: 645px; height: 1px; background: #7a797f; }
  .copyright { left: 38px; top: 196px; font-size: 13.5px; color: var(--footer-muted); }
  .copyright b { color: var(--footer-text); font-weight: 400; }
</style>
</head>
<body>
<main class="sheet">
  <header>
    <div class="abs header-photo" role="img" aria-label="Beach scene with sky and turquoise ocean"></div>
    <div class="abs brand-name">Varnell at the Shore</div>
    <div class="abs tagline">SELL WITH THE BEST</div>
  </header>

  <section class="intro">
    <h2 class="abs section-title" style="left:38px; top:303px;">LARGER ITEM HEADING</h2>
    <p class="abs body-text" style="left:38px; top:342px; width:455px;">Lorem ipsum dolor sit amet, consectetur adipiscing elit. Duis quis lectus at arcu egestas fringilla fermentum eget ipsum. Vestibulum hendrerit dignissim nunc vel volutpat. Nulla facilisi. Lorem ipsum dolor sit amet, consectetur adipiscing elit. Duis quis lectus at arcu egestas fringilla fermentum eget ipsum. Vestibulum hendrerit dignissim nunc vel volutpat. Nulla facilisi. Lorem ipsum dolor sit amet, consectetur adipiscing elit.</p>
    <div class="abs agent-photo" role="img" aria-label="Portrait of agent Reed Varnell"></div>
    <div class="abs agent-name">Reed Varnell</div>
    <div class="abs agent-email">Email Me</div>
  </section>
  <div class="abs rule" style="top:578px;"></div>

  <section class="market">
    <h2 class="abs section-title" style="left:38px; top:618px;">MARKET DATA</h2>
    <p class="abs body-text" style="left:38px; top:657px; width:650px; height:121px; overflow:hidden;">Lorem ipsum dolor sit amet, consectetur adipiscing elit. Duis quis lectus at arcu egestas fringilla fermentum eget ipsum. Vestibulum hendrerit dignissim nunc vel volutpat. Nulla facilisi. Lorem ipsum dolor sit amet, consectetur adipiscing elit. Duis quis lectus at arcu egestas fringilla fermentum eget ipsum. Vestibulum hendrerit dignissim nunc vel volutpat. Nulla facilisi. Lorem ipsum dolor sit amet, consectetur</p>
    <h3 class="abs snapshot-title">December 2013 Snapshot</h3>
    <table class="abs market-table">
      <tr><th class="label">Zip Code:</th><th>92677</th><th>92651</th><th>92672</th><th>92673</th><th>92629</th></tr>
      <tr><td class="label">Monthly Units Sold</td><td>115</td><td>116</td><td>117</td><td>118</td><td>119</td></tr>
      <tr><td class="label">Avg. Sold Price</td><td>$583K</td><td>$583K</td><td>$583K</td><td>$583K</td><td>$583K</td></tr>
      <tr><td class="label">Sold % of Orig List $</td><td>95.5%</td><td>95.5%</td><td>95.5%</td><td>95.5%</td><td>95.5%</td></tr>
      <tr><td class="label">Current Units Listed</td><td>122</td><td>122</td><td>122</td><td>122</td><td>122</td></tr>
      <tr><td class="label">Avg. List Price</td><td>$1,415K</td><td>$1,415K</td><td>$1,415K</td><td>$1,415K</td><td>$1,415K</td></tr>
      <tr><td class="label">Avg. Days on Market</td><td>83</td><td>83</td><td>83</td><td>83</td><td>83</td></tr>
      <tr class="trend-row">
        <td class="label" style="vertical-align:middle;">Historical Trends</td>
        <td><span class="trend"><svg width="46" height="34" viewBox="0 0 46 34"><rect x="1" y="1" width="44" height="32" fill="#fff" stroke="#bbb"/><rect x="8" y="14" width="8" height="16" fill="#1d5a66"/><rect x="19" y="10" width="8" height="20" fill="#1d5a66"/><rect x="30" y="6" width="8" height="24" fill="#1d5a66"/></svg><a>see charts</a></span></td>
        <td><span class="trend"><svg width="46" height="34" viewBox="0 0 46 34"><rect x="1" y="1" width="44" height="32" fill="#fff" stroke="#bbb"/><rect x="8" y="14" width="8" height="16" fill="#1d5a66"/><rect x="19" y="10" width="8" height="20" fill="#1d5a66"/><rect x="30" y="6" width="8" height="24" fill="#1d5a66"/></svg><a>see charts</a></span></td>
        <td><span class="trend"><svg width="46" height="34" viewBox="0 0 46 34"><rect x="1" y="1" width="44" height="32" fill="#fff" stroke="#bbb"/><rect x="8" y="14" width="8" height="16" fill="#1d5a66"/><rect x="19" y="10" width="8" height="20" fill="#1d5a66"/><rect x="30" y="6" width="8" height="24" fill="#1d5a66"/></svg><a>see charts</a></span></td>
        <td><span class="trend"><svg width="46" height="34" viewBox="0 0 46 34"><rect x="1" y="1" width="44" height="32" fill="#fff" stroke="#bbb"/><rect x="8" y="14" width="8" height="16" fill="#1d5a66"/><rect x="19" y="10" width="8" height="20" fill="#1d5a66"/><rect x="30" y="6" width="8" height="24" fill="#1d5a66"/></svg><a>see charts</a></span></td>
        <td><span class="trend"><svg width="46" height="34" viewBox="0 0 46 34"><rect x="1" y="1" width="44" height="32" fill="#fff" stroke="#bbb"/><rect x="8" y="14" width="8" height="16" fill="#1d5a66"/><rect x="19" y="10" width="8" height="20" fill="#1d5a66"/><rect x="30" y="6" width="8" height="24" fill="#1d5a66"/></svg><a>see charts</a></span></td>
      </tr>
    </table>
  </section>
  <div class="abs rule" style="top:1080px;"></div>

  <section class="listings">
    <h2 class="abs section-title" style="left:38px; top:1114px;">FEATURED LISTINGS</h2>

    <div class="abs listing-photo" style="top:1168px;" role="img" aria-label="Sunny patio with umbrella and dining set"></div>
    <h3 class="abs listing-title" style="top:1164px;">2180 Harbor Shell Way, Dana Point, CA 92629</h3>
    <p class="abs body-text listing-text" style="top:1200px;">Lorem ipsum dolor sit amet, consectetur adipiscing elit. Duis quis lectus at arcu egestas fringilla fermentum eget ipsum. Vestibulum hendrerit dignissim nunc vel volutpat. Nulla facilisi.</p>
    <a class="abs read-more" style="left:319px; top:1345px;">READ MORE</a>

    <div class="abs listing-photo" style="top:1393px;" role="img" aria-label="Sunny patio with umbrella and dining set"></div>
    <h3 class="abs listing-title" style="top:1388px;">2180 Harbor Shell Way, Dana Point, CA 92629</h3>
    <p class="abs body-text listing-text" style="top:1424px;">Lorem ipsum dolor sit amet, consectetur adipiscing elit. Duis quis lectus at arcu egestas fringilla fermentum eget ipsum. Vestibulum hendrerit dignissim nunc vel volutpat. Nulla facilisi.</p>
    <a class="abs read-more" style="left:319px; top:1570px;">READ MORE</a>
  </section>
  <div class="abs rule" style="top:1620px;"></div>

  <section class="news">
    <h2 class="abs section-title" style="left:38px; top:1654px;">NEWS</h2>

    <h3 class="abs news-title" style="top:1703px;">Southern California's luxury housing market rebounds</h3>
    <p class="abs body-text news-text" style="top:1736px;">Lorem ipsum dolor sit amet, consectetur adipiscing elit. Duis quis lectus at arcu egestas fringilla fermentum eget ipsum. Vestibulum hendrerit dignissim nunc vel volutpat. Nulla facilisi.</p>
    <a class="abs read-more" style="left:41px; top:1822px;">READ MORE</a>

    <h3 class="abs news-title" style="top:1867px;">Southern California's luxury housing market rebounds</h3>
    <p class="abs body-text news-text" style="top:1900px;">Lorem ipsum dolor sit amet, consectetur adipiscing elit. Duis quis lectus at arcu egestas fringilla fermentum eget ipsum. Vestibulum hendrerit dignissim nunc vel volutpat. Nulla facilisi.</p>
    <a class="abs read-more" style="left:41px; top:1986px;">READ MORE</a>
  </section>
  <div class="abs rule" style="top:2030px;"></div>

  <section class="events">
    <h2 class="abs section-title" style="left:38px; top:2064px;">UPCOMING OC EVENTS</h2>
    <div class="abs event" style="left:41px; top:2108px;">
      <div class="event-date">MAR<b>08</b></div>
      <div>
        <h3 class="event-title">Harbor Art Walk</h3>
        <p class="event-text">Lorem ipsum dolor sit amet, consectetur.</p>
      </div>
    </div>
    <div class="abs event" style="left:365px; top:2108px;">
      <div class="event-date">MAR<b>22</b></div>
      <div>
        <h3 class="event-title">Beachfront Wine Evening</h3>
        <p class="event-text">Lorem ipsum dolor sit amet, consectetur.</p>
      </div>
    </div>
  </section>
  <div class="abs rule" style="top:2194px;"></div>

  <section class="connect">
    <h2 class="abs connect-title">STAY CONNECTED</h2>
    <div class="abs social-list" aria-label="Social links">
      <span class="social-dot"><svg viewBox="0 0 24 24"><rect x="3" y="6" width="18" height="12" rx="1"/><path d="M3 7l9 6 9-6"/></svg></span>
      <span class="social-dot"><svg viewBox="0 0 24 24"><path d="M4 5h16v11H9l-5 4z"/></svg></span>
      <span class="social-dot"><svg viewBox="0 0 24 24"><circle cx="6" cy="12" r="2.5"/><circle cx="18" cy="6" r="2.5"/><circle cx="18" cy="18" r="2.5"/><path d="M8.2 11l7.6-4M8.2 13l7.6 4"/></svg></span>
      <span class="social-dot"><svg viewBox="0 0 24 24"><path d="M12 21s-7-6.5-7-11a7 7 0 0 1 14 0c0 4.5-7 11-7 11z"/><circle cx="12" cy="10" r="2.5"/></svg></span>
      <span class="social-dot"><svg viewBox="0 0 24 24"><path d="M12 5v14M5 12h14"/></svg></span>
      <span class="social-dot"><svg viewBox="0 0 24 24"><circle cx="12" cy="12" r="9"/><path d="M3 12h18M12 3c3 3 3 15 0 18M12 3c-3 3-3 15 0 18"/></svg></span>
      <span class="social-dot"><svg viewBox="0 0 24 24"><circle cx="12" cy="8" r="4"/><path d="M4 21c1-5 15-5 16 0"/></svg></span>
      <span class="social-dot"><svg viewBox="0 0 24 24"><path d="M10 14a4 4 0 0 0 6 0l3-3a4 4 0 0 0-6-6l-1 1M14 10a4 4 0 0 0-6 0l-3 3a4 4 0 0 0 6 6l1-1"/></svg></span>
    </div>
  </section>

  <footer class="abs footer">
    <p class="abs footer-text">Lorem ipsum dolor sit amet, consectetur adipiscing elit. Sed commodo est id nulla luctus, quis posuere metus elementum. Phasellus elementum tortor nec massa pellentesque lobortis.</p>
    <div class="abs footer-rule"></div>
    <p class="abs copyright">Copyright 2014 <b>Varnell Shore</b>. All Rights Reserved.</p>
  </footer>
</main>
</body>
</html>
```